Website design for respected, long standing real estate development company in Central Oregon

Uncoded PSD design only. Homepage and one interior sample page.

Updated website design needed for Halvard Holdings, one of Central Oregon’s oldest and most respected real estate development companies. They develop communities that focus on natural beauty and upscale amenities.

They need a website that features their long, unique history and their current efforts to build smart, healthy and livable communities. They need to tell their story to those who aren't familiar with the company. They need to build credibility and set themselves apart from other real estate development companies.

Current site: http://halvard-holdings.example/

Target Market(s)

Target market is people who are new or plan to relocate to Central Oregon and are researching communities they want to live in.
Secondary markets are potential project partners, and the media. They need to build credibility with these audiences.
The site also needs to be easy to use for non-profits seeking contributions.

Industry/Entity Type

Real Estate Development

Number of Pages Required

Font styles to use
Sans Serif

Requirements
Must have
• Must have simple, user-friendly navigation with organized content.
• Design must be fresh, light and modern.
• Design must use great, high impact imagery that promotes the Central Oregon lifestyle.
• Design must highlight current and future communities and encourage click-throughs to those specific websites.
• Include video element.
• Include social links.
• Do not use dummy copy/lorum ipsum. Use copy from the current site instead. Use correct phone number, address, etc.
Should not have
• Lorum ipsum/dummy copy

```html
<!DOCTYPE html>
<html lang="en">
<head>
<meta charset="utf-8">
<title>Halvard Holdings Corporation</title>
<link rel="stylesheet" href="https://fonts.googleapis.com/css2?family=Raleway:wght@400;500;600;700&family=Open+Sans:wght@400;600;700&display=swap">
<style>
:root{
  --ink:#333;
  --muted:#666;
  --plum:#4a1f3b;
  --header:#3a3a3a;
  --footer:#3d3d3d;
  --legal:#4a1d33;
  --light:#f4f4f4;
  --band:#e2e4e6;
  --white:#fff;
  --black:#111;
}
*{box-sizing:border-box;margin:0;padding:0}
html,body{width:1200px;height:4639px;overflow:hidden}
body{position:relative;font-family:"Open Sans",Arial,sans-serif;color:var(--ink);background:var(--white)}
.abs{position:absolute}
section,header,footer{position:absolute;left:0;width:1200px;overflow:hidden}
.heading{font-family:"Raleway",Arial,sans-serif;font-weight:600;color:var(--plum);text-align:center;letter-spacing:1px}
.btn{position:absolute;display:flex;align-items:center;justify-content:center;font-family:"Open Sans",Arial,sans-serif;font-size:16px;letter-spacing:.5px}
.btn-outline{border:2px solid #222;color:#222;background:var(--white)}
.btn-dark{background:var(--black);color:var(--white)}
/* header */
.site-header{top:0;height:210px;background:var(--header)}
.brand{left:0;width:1200px;top:38px;display:flex;justify-content:center;align-items:center;gap:14px}
.brand-mark{width:44px;height:44px;background:var(--white)}
.brand-name{font-family:"Raleway",Arial,sans-serif;font-size:24px;font-weight:600;color:var(--white)}
.main-nav{top:132px;left:145px;display:flex;gap:0}
.main-nav a{font-family:"Raleway",Arial,sans-serif;font-size:15px;color:var(--white);text-decoration:none;padding:12px 22px;letter-spacing:.5px}
.main-nav a.active{background:var(--white);color:#222}
/* hero */
.hero{top:210px;height:579px;background:linear-gradient(100deg,#2d4f79 0%,#5f7fa6 30%,#b89a78 60%,#7a5c46 85%,#3e3b45 100%)}
.hero-title{top:235px;left:0;width:1200px;text-align:center;font-family:"Raleway",Arial,sans-serif;font-size:48px;font-weight:500;color:var(--white);letter-spacing:1px}
.hero .btn{left:495px;top:330px;width:210px;height:56px;border:2px solid var(--white);color:var(--white);font-size:15px}
.dots{display:flex;gap:14px}
.dots span{width:14px;height:14px;border-radius:50%;background:var(--white)}
.dots span.on{box-shadow:0 0 0 3px rgba(255,255,255,.5)}
.hero .dots{left:537px;top:491px}
/* about */
.about{top:789px;height:485px}
.about .h1{top:58px;left:0;width:1200px;font-size:40px}
.about .h2{top:110px;left:0;width:1200px;font-size:34px;color:#2a2a2a}
.about p{top:168px;left:170px;width:860px;text-align:center;font-size:15px;line-height:29px;color:#8a8a8a}
.about .btn{left:495px;top:367px;width:210px;height:52px}
/* development */
.development{top:1274px;height:659px;background:var(--band)}
.development .heading{top:56px;left:0;width:1200px;font-size:40px}
.card{position:absolute;top:139px;width:250px;text-align:center}
.card .photo{height:164px}
.card h3{margin-top:28px;font-family:"Raleway",Arial,sans-serif;font-size:21px;font-weight:500;color:#222;line-height:24px}
.card p{margin-top:14px;font-size:14px;line-height:22px;color:#444;padding:0 8px}
.card .btn{position:absolute;left:40px;top:396px;width:160px;height:50px}
/* real estate */
.sale{top:1933px;height:334px;background:linear-gradient(90deg,#1e2420,#3c3f3e 55%,#2a2a2a)}
.sale .photo{left:0;top:0;width:597px;height:334px;background:linear-gradient(135deg,#3a4a3c,#6a8a5e 50%,#2d3a2f)}
.sale h2{left:650px;top:56px;font-family:"Raleway",Arial,sans-serif;font-size:40px;font-weight:500;color:var(--white)}
.sale p{left:652px;top:120px;width:480px;font-size:14px;line-height:24px;color:#ddd}
.sale .btn{left:650px;top:265px;width:160px;height:50px}
/* rentals */
.rentals{top:2267px;height:603px;background:var(--light)}
.rentals .heading{top:112px;left:0;width:1200px;font-size:40px}
.rentals .photo{left:84px;top:217px;width:411px;height:278px;background:linear-gradient(120deg,#8d6a4d,#d9c3a2 50%,#7aa3c6)}
.rentals h3{left:520px;top:243px;font-family:"Raleway",Arial,sans-serif;font-size:20px;font-weight:700;color:#222}
.rentals p{left:520px;top:285px;width:600px;font-size:14px;line-height:25px;color:#555}
.rentals p a{color:#444;font-style:normal;text-decoration:underline}
/* video */
.video{top:2870px;height:418px;background:linear-gradient(180deg,#3c4050,#6a4f3c 55%,#2f2a2a)}
.video svg{left:557px;top:137px}
.video .label{left:0;top:267px;width:1200px;text-align:center;color:var(--white);font-family:"Raleway",Arial,sans-serif;font-weight:700;font-size:16px;letter-spacing:.5px}
/* resources */
.resources{top:3288px;height:340px}
.resources .heading{top:58px;left:0;width:1200px;font-size:40px}
.partners{top:124px;left:240px;width:740px;display:flex;align-items:center;height:100px}
.partner{flex:1;display:flex;align-items:center;justify-content:center;gap:10px;font-family:"Raleway",Arial,sans-serif;font-size:18px;font-weight:600;color:#333;height:100px;border-right:1px solid #ccc}
.partner:last-child{border-right:none}
.partner i{width:26px;height:26px;border-radius:50%;background:#555;display:block}
.resources .dots{left:557px;top:255px}
.resources .dots span{background:#888}
.resources .dots span.on{background:#333;box-shadow:0 0 0 3px #ccc}
/* contact */
.contact{top:3628px;height:625px;background:linear-gradient(180deg,#3d3935,#5d4e44 45%,#2e2b29)}
.contact h2{left:0;top:58px;width:1200px;text-align:center;font-family:"Raleway",Arial,sans-serif;font-size:42px;font-weight:400;color:var(--white)}
.contact .intro{left:0;top:115px;width:1200px;text-align:center;font-size:16px;color:#eee}
.field{position:absolute;border:1px solid #ddd;color:#eee;font-size:14px;padding:14px 12px}
.captcha{left:887px;top:232px;width:134px;height:53px;background:var(--white);display:flex;align-items:center;justify-content:center;font-family:"Raleway",Arial,sans-serif;font-style:normal;font-size:20px;letter-spacing:3px;color:#333}
.contact .btn{left:495px;top:510px;width:207px;height:47px;background:var(--white);color:#111;font-weight:700}
/* footer */
.site-footer{top:4253px;height:331px;background:var(--footer);color:#ddd}
.col-title{position:absolute;top:62px;font-family:"Raleway",Arial,sans-serif;font-size:20px;color:var(--white)}
.foot-nav{position:absolute;top:108px;font-size:13px;line-height:40px}
.foot-nav li{list-style:none}
.foot-nav li::before{content:"» ";color:#aaa}
.post{position:absolute;left:340px;display:flex;gap:12px;font-size:12px;line-height:17px}
.post .thumb{width:58px;height:50px}
.post b{display:block;font-weight:600;color:var(--white)}
.news input{position:absolute;left:609px;width:222px;height:40px;background:transparent;border:1px solid #ccc;color:#ddd;font-size:13px;padding:0 10px;font-family:inherit}
.news .btn{left:609px;top:218px;width:160px;height:48px;background:var(--black);color:var(--white);font-size:14px}
.addr{position:absolute;left:872px;font-size:14px;line-height:22px;color:#ddd}
.legal{position:absolute;left:0;top:4584px;width:1200px;height:55px;background:var(--legal);color:#eee;font-size:12px;display:flex;align-items:center;justify-content:center}
.legal b{margin:0 4px}
</style>
</head>
<body>

<header class="site-header">
  <div class="abs brand"><span class="brand-mark"></span><span class="brand-name">Halvard Holdings Corporation</span></div>
  <nav class="abs main-nav">
    <a class="active" href="#">HOME</a><a href="#">DEVELOPMENT</a><a href="#">SALES</a><a href="#">RENTALS</a><a href="#">RESOURCES</a><a href="#">BLOG</a><a href="#">ABOUT</a><a href="#">CONTACT</a>
  </nav>
</header>

<section class="hero" role="img" aria-label="Modern home terrace with lounge furniture at dusk">
  <h1 class="abs hero-title">WELCOME TO HALVARD HOLDINGS</h1>
  <a class="btn" href="#">CONTACT US</a>
  <div class="abs dots"><span class="on"></span><span></span><span></span><span></span></div>
</section>

<section class="about">
  <h2 class="abs heading h1">ABOUT</h2>
  <h2 class="abs heading h2">HALVARD HOLDINGS</h2>
  <p class="abs">Central Oregon real estate developer Halvard Holdings Corporation has created some of Central Oregon's most recognizable real estate communities, including Westfield Commons, Canyon Rim, RiverRun, Alder Butte, Alder Glen, Summit Pines Village Resort, and Ironridge in Prineville. Halvard Holdings takes great pride in its long history in Central Oregon, but has always maintained a solid vision of the future of Central Oregon's communities. With each new real estate development, Halvard Holdings continues to demonstrate its commitment to creating environmentally sensitive communities, fostering a way of life we can all live with for generations to come.</p>
  <a class="btn btn-outline" href="#">CONTACT US</a>
</section>

<section class="development">
  <h2 class="abs heading">DEVELOPMENT</h2>
  <div class="card" style="left:77px">
    <div class="photo" role="img" aria-label="Craftsman style home with lawn" style="background:linear-gradient(180deg,#6f9cc9,#9c8468 60%,#5d7a3e)"></div>
    <h3>IRONRIDGE</h3>
    <p>Prineville Oregon There's something about the West that still inspires freedom and possibility....</p>
    <a class="btn btn-dark" href="#">READ MORE</a>
  </div>
  <div class="card" style="left:343px">
    <div class="photo" role="img" aria-label="Mountain peak above pine forest" style="background:linear-gradient(180deg,#8ba7c6,#b7a58c 50%,#4f5e3a)"></div>
    <h3>SUMMIT PINES<br>VILLAGE RESORT</h3>
    <p>Summit Pines Village Resort features a variety of on-site amenities, including a heated pool, two outdoor...</p>
    <a class="btn btn-outline" href="#">READ MORE</a>
  </div>
  <div class="card" style="left:609px">
    <div class="photo" role="img" aria-label="Canyon view at sunset" style="background:linear-gradient(180deg,#c7a27a,#8a6a4c 55%,#3e4a34)"></div>
    <h3>CANYON RIM</h3>
    <p>Discover Canyon Rim, an environmentally sensitive real estate development by Halvard Holdings offering...</p>
    <a class="btn btn-outline" href="#">READ MORE</a>
  </div>
  <div class="card" style="left:875px">
    <div class="photo" role="img" aria-label="Tree-lined neighborhood street" style="background:linear-gradient(180deg,#7fa6d4,#6d7f5a 55%,#5a5a58)"></div>
    <h3>WESTFIELD<br>COMMONS</h3>
    <p>There's something about the West that still inspires freedom and possibility. Wild rivers and rugged...</p>
    <a class="btn btn-outline" href="#">READ MORE</a>
  </div>
</section>

<section class="sale">
  <div class="abs photo" role="img" aria-label="Lawn and trees seen through tall windows"></div>
  <h2 class="abs">REAL ESTATE SALE</h2>
  <p class="abs">Halvard Holdings Realty, established in Bend, Oregon in 1975, has a long track record in Central Oregon real estate. Canyon Rim is the current Halvard Holdings development offered by Halvard Holdings Realty. Luxury home lots over one acre in size grace the north side of Alder Butte and offer panoramic views of the Cascade Mountains.</p>
  <a class="btn btn-dark" href="#">READ MORE</a>
</section>

<section class="rentals">
  <h2 class="abs heading">VACATION RENTALS</h2>
  <div class="abs photo" role="img" aria-label="Bright resort living room with tall windows"></div>
  <h3 class="abs">SUMMIT PINES VILLAGE RESORT</h3>
  <p class="abs">Looking for the perfect place to live or vacation? Summit Pines Village Resort is the answer — situated on 170 forested acres of a bluff overlooking the Deschutes River in Bend. A truly exceptional vacation or full-time residence, this resort features fully appointed condominium lodging, several with breathtaking Deschutes River views, and year-round amenities in a pristine forest setting. <a href="#">Summit Pines Village Resort</a> website to learn more or to book your next vacation...</p>
</section>

<section class="video" role="img" aria-label="Aerial canyon landscape video still">
  <svg class="abs" width="86" height="86" viewBox="0 0 86 86" aria-hidden="true"><circle cx="43" cy="43" r="40" fill="none" stroke="#fff" stroke-width="4"/><path d="M34 26 L62 43 L34 60 Z" fill="#fff"/></svg>
  <div class="abs label">WHATCH VIDEO</div>
</section>

<section class="resources">
  <h2 class="abs heading">PROPERTY OWNER RESOURCES</h2>
  <div class="abs partners">
    <div class="partner"><i></i>Alder Butte</div>
    <div class="partner">Ironridge</div>
    <div class="partner"><i></i>Westfield Commons</div>
  </div>
  <div class="abs dots"><span class="on"></span><span></span><span></span></div>
</section>

<section class="contact" role="img" aria-label="Canyon landscape behind the contact form">
  <h2 class="abs">CONTACT US</h2>
  <div class="abs intro">For additional details on Halvard Holdings, or to schedule a property visit, please contact us at:</div>
  <div class="field" style="left:176px;top:173px;width:421px;height:53px">Name:</div>
  <div class="field" style="left:603px;top:173px;width:418px;height:53px">E-Mail:</div>
  <div class="field" style="left:176px;top:232px;width:421px;height:53px">City of Residence:</div>
  <div class="field" style="left:603px;top:232px;width:270px;height:53px">Captcha code:</div>
  <div class="abs captcha">xk7mq</div>
  <div class="field" style="left:176px;top:300px;width:845px;height:186px">Message:</div>
  <a class="btn" href="#">SUBMIT</a>
</section>

<footer class="site-footer">
  <div class="col-title" style="left:77px">Navigation</div>
  <ul class="foot-nav" style="left:77px"><li>Home</li><li>Development</li><li>Resources</li><li>About</li></ul>
  <ul class="foot-nav" style="left:212px"><li>Sales</li><li>Rentals</li><li>Blog</li><li>Contact</li></ul>

  <div class="col-title" style="left:340px">Blog</div>
  <div class="post" style="top:110px"><div class="thumb" role="img" aria-label="Home exterior" style="background:linear-gradient(#7fa3c8,#6b6a4a)"></div><div><b>IRONRIDGE</b>Prineville Oregon There's<br>something about</div></div>
  <div class="post" style="top:185px"><div class="thumb" role="img" aria-label="Canyon view" style="background:linear-gradient(#c7a27a,#4f5a3a)"></div><div><b>CANYON RIM</b>Prineville Oregon There's<br>something about</div></div>

  <div class="col-title" style="left:609px">News letter</div>
  <div class="news">
    <input style="top:108px" value="User Name*" aria-label="User name">
    <input style="top:160px" value="Email" aria-label="Email">
    <a class="btn" href="#">SUBSCRIBE</a>
  </div>

  <div class="col-title" style="left:872px">Address</div>
  <svg class="abs" style="left:872px;top:112px" width="20" height="26" viewBox="0 0 20 26" aria-hidden="true"><path d="M10 0C4.5 0 0 4.4 0 9.8 0 17 10 26 10 26s10-9 10-16.2C20 4.4 15.5 0 10 0z" fill="#fff"/><circle cx="10" cy="10" r="3.5" fill="#3d3d3d"/></svg>
  <div class="addr" style="left:905px;top:108px">Halvard Holdings Corporation<br>220 NW Juniper Avenue<br>Bend, Oregon 97701</div>
  <svg class="abs" style="left:872px;top:200px" width="20" height="20" viewBox="0 0 24 24" aria-hidden="true"><path d="M6.6 10.8c1.4 2.8 3.8 5.1 6.6 6.6l2.2-2.2c.3-.3.7-.4 1-.2 1.1.4 2.3.6 3.6.6.6 0 1 .4 1 1V20c0 .6-.4 1-1 1C10.6 21 3 13.4 3 4c0-.6.4-1 1-1h3.5c.6 0 1 .4 1 1 0 1.3.2 2.5.6 3.6.1.3 0 .7-.2 1z" fill="#fff"/></svg>
  <div class="addr" style="left:905px;top:199px">541-555-0142</div>
</footer>
<div class="legal">Copyright 2016 <b>Halvard Holdings corporations</b> All rights reserved.</div>

</body>
</html>
```